Business card design for QuelMarvion

I need a business card based on the logo design produced for QuelMarvion. The company is focused on triathlon and endurance sport coaching and the tag line is (per the logo) "Endurance. Resilience. Achievement". The design should be sophisticated, appropriate to an affluent and business oriented target market. Colors are optional but the color of the logo probably dictates the color used on the card. I envisage using the red logo, with black print for the wording and contact numbers on a white or cream background, but am open to alternative suggestions. I expect to select something fairly conventional, but would like to see some designs that are less conventional to stretch my thinking on what could be appropriate. I am assuming a single side design is best, but willing to consider double sided as an option.

Target Market(s)

Individual athletes and corporate health and wellness leaders

Industry/Entity Type

Health And Wellness

Contact Information for Business Card

The card should provide the following information:
Logo
My name: Gordon Lashby
Company website: QuelMarvion.com
My email: gordon.lashby@quelmarvion.com
My cell phone number: +1-555-018-2739

Font styles to use
Sans Serif

Colors

Designer to choose colors to be used in the design.

Requirements
Must have
• Space on the card - simple design, not over crowded.
Nice to have
• clean and clear font, nothing garish or mass market like
Should not have
• Do not add pictures

```html
<!DOCTYPE html>
<html lang="en">
<head>
<meta charset="utf-8">
<title>QuelMarvion Business Card</title>
<link rel="stylesheet" href="https://fonts.googleapis.com/css2?family=Fira+Sans:wght@600&family=Overpass:wght@600;700&family=Roboto:wght@400&display=swap">
<style>
  :root {
    --backdrop: #b8b8b8;
    --card-white: #f3f3f3;
    --brand-red: #ad2729;
    --on-red: #ffffff;
  }
  * { margin: 0; padding: 0; box-sizing: border-box; }
  html, body {
    width: 1200px;
    height: 960px;
    overflow: hidden;
    background: var(--backdrop);
  }
  .canvas {
    position: relative;
    width: 1200px;
    height: 960px;
  }
  .card {
    position: absolute;
    left: 313px;
    width: 600px;
    height: 342px;
    box-shadow: 2px 3px 4px rgba(0,0,0,0.3);
    text-align: center;
  }
  .card-front {
    top: 123px;
    background: var(--card-white);
  }
  .card-back {
    top: 525px;
    background: var(--brand-red);
    color: var(--on-red);
  }
  .brand-name {
    position: absolute;
    left: 0; right: 0;
    top: 148px;
    font-family: "Fira Sans", sans-serif;
    font-weight: 600;
    font-size: 47px;
    line-height: 1;
    color: var(--brand-red);
    letter-spacing: 0.2px;
  }
  .brand-dot {
    position: absolute;
    left: 288px;
    top: 90px;
    width: 24px;
    height: 24px;
    border-radius: 50%;
    background: var(--on-red);
  }
  .holder-name {
    position: absolute;
    left: 0; right: 0;
    top: 134px;
    font-family: "Overpass", sans-serif;
    font-weight: 700;
    font-size: 22px;
    line-height: 1;
  }
  .holder-role {
    position: absolute;
    left: 0; right: 0;
    top: 161px;
    font-family: "Overpass", sans-serif;
    font-weight: 600;
    font-size: 15px;
    line-height: 1;
  }
  .contact-list {
    position: absolute;
    left: 0; right: 0;
    top: 191px;
    list-style: none;
    font-family: "Roboto", sans-serif;
    font-weight: 400;
    font-size: 14px;
    line-height: 19.5px;
  }
</style>
</head>
<body>
  <main class="canvas">
    <section class="card card-front">
      <div class="brand-name">QuelMarvion</div>
    </section>
    <section class="card card-back">
      <span class="brand-dot" aria-hidden="true"></span>
      <div class="holder-name">Gordon Lashby</div>
      <div class="holder-role">Triathlete</div>
      <ul class="contact-list">
        <li>+1-555-018-2739</li>
        <li>gordon.lashby@quelmarvion.com</li>
        <li>www.QuelMarvion.com</li>
      </ul>
    </section>
  </main>
</body>
</html>
```